Marlo Tidy Yard Website

We need a website design for this new company. I've attached the company logo. This company is in the construction industry that provides general labor, maintenance and cleaning for construction sites. We want a clean and simple website that can be easy to navigate.

Target Market(s)

Construction industry

Industry/Entity Type

Construction

Number of Pages Required

2 page

Font styles to use
Sans Serif

```html
<!DOCTYPE html>
<html lang="en">
<head>
<meta charset="utf-8">
<title>Marlo Tidy Yard – Construction Site Labor, Maintenance &amp; Cleanup</title>
<link href="https://fonts.googleapis.com/css2?family=Poppins:ital,wght@0,400;0,600;0,700;1,400;1,600;1,700&family=Open+Sans:wght@400;600;700&display=swap" rel="stylesheet">
<style>
:root{
  --navy:#163463;
  --blue:#1f6fc8;
  --cyan:#19bde6;
  --yellow:#ffe426;
  --orange:#f26b1d;
  --pale:#eef1fb;
  --ink:#1c2233;
  --muted:#6b7487;
  --stage:#bdbdbd;
}
*{margin:0;padding:0;box-sizing:border-box}
html,body{width:960px;height:1200px;overflow:hidden}
body{background:radial-gradient(circle at 50% 45%,#d9d9d9,var(--stage));font-family:'Open Sans',sans-serif;color:var(--ink)}
.stage{position:absolute;left:0;top:0;width:1200px;height:1500px;transform:scale(.8);transform-origin:0 0}
.page{position:absolute;left:352px;top:0;width:458px;height:1500px;background:#fff;overflow:hidden}
.abs{position:absolute}
.head{position:absolute;left:0;top:0;width:458px;height:47px;background:var(--navy)}
.head .logo-bg{position:absolute;left:0;top:0;width:145px;height:47px;background:#fff;clip-path:polygon(0 0,100% 0,70% 100%,0 100%)}
.brand{position:absolute;left:12px;top:17px;display:flex;align-items:center;gap:4px;font:700 9.5px 'Poppins',sans-serif;color:var(--navy);white-space:nowrap}
.brand i{display:block;width:9px;height:9px;background:var(--orange)}
.info{position:absolute;top:14px;font-size:6px;color:#fff;line-height:1.45;white-space:nowrap}
.info b{font-weight:700;font-size:5.5px;display:block}
.info .phone{font:700 10px 'Poppins',sans-serif;color:var(--yellow)}
.nav{position:absolute;top:47px;left:0;width:458px;height:23px;background:#fff;display:flex;align-items:center;padding-left:23px;gap:19px;font:600 6px 'Poppins',sans-serif}
.nav .on{color:var(--blue)}
.quote{position:absolute;right:13px;top:50px;width:61px;height:16px;border-radius:8px;background:var(--navy);color:#fff;font:700 5px 'Poppins',sans-serif;display:flex;align-items:center;justify-content:center}
.hero{position:absolute;top:70px;left:0;width:458px;height:172px;background:linear-gradient(100deg,#5d6a72,#a7b0b4 40%,#d7d9d6 60%,#8d959b)}
.seal{position:absolute;left:50px;top:15px;width:112px;height:96px;border-radius:50%;background:var(--yellow);text-align:center;padding-top:32px}
.seal h3{font:700 8.5px 'Poppins',sans-serif;color:var(--ink)}
.seal p{font:italic 5px 'Poppins',sans-serif;color:#444;line-height:1.3}
.seal span{display:inline-block;margin-top:6px;background:var(--blue);color:#fff;font:700 4px 'Poppins',sans-serif;padding:3px 11px;border-radius:6px}
.disc{position:absolute;left:126px;top:5px;width:44px;height:44px;border-radius:50%;background:var(--cyan);color:#fff;text-align:center;font:700 4px 'Poppins',sans-serif;padding-top:8px;line-height:1.1}
.disc b{font-size:12px;display:block;color:#fff}
.arrow{position:absolute;top:53px}
.tabs{position:absolute;left:13px;top:190px;width:432px;height:52px;display:flex}
.tab{flex:1;padding:13px 0 0 18px;font:700 12px 'Poppins',sans-serif;color:#fff;line-height:1.1;white-space:nowrap}
.tab em{display:block;font:italic 400 8.5px 'Poppins',sans-serif}
.t1{background:var(--navy)}.t1 em{color:var(--cyan)}
.t2{background:var(--blue)}.t2 em{color:var(--yellow)}
.t3{background:var(--cyan)}.t3 em{color:var(--yellow)}
.t4{background:var(--yellow);color:var(--navy)}.t4 em{color:var(--blue)}
.ph{position:absolute;border-radius:50%;overflow:hidden}
.kicker{font:italic 8px 'Poppins',sans-serif;color:var(--blue)}
.title{font:700 14.5px 'Poppins',sans-serif;color:var(--ink);line-height:1.25}
.para{font-size:6px;color:var(--muted);line-height:1.6}
.btn-y{position:absolute;background:var(--yellow);border-radius:11px;font:700 5.5px 'Poppins',sans-serif;color:var(--navy);display:flex;align-items:center;justify-content:center}
.work{position:absolute;top:450px;left:0;width:458px;height:300px;background:var(--pale)}
.center{position:absolute;left:0;width:458px;text-align:center}
.step-badge{position:absolute;width:40px;height:34px;border-radius:50%;font:italic 600 7.5px 'Poppins',sans-serif;display:flex;align-items:center;justify-content:center}
.step-t{position:absolute;width:130px;text-align:center;font:italic 700 9.5px 'Poppins',sans-serif}
.step-p{position:absolute;width:104px;text-align:center;font-size:6px;color:var(--muted);line-height:1.6}
.step-p a{color:var(--blue);text-decoration:none}
.feat{position:absolute;top:735px;left:0;width:458px;height:270px;background:linear-gradient(180deg,#27508a,var(--navy) 70%)}
.card{position:absolute;top:123px;width:134px;height:82px}
.card-l{position:absolute;top:215px;width:134px;text-align:center;font:700 8px 'Poppins',sans-serif;color:#fff}
.dots{position:absolute;top:256px;left:216px;display:flex;gap:5px}
.dots i{width:4px;height:4px;border-radius:50%;background:#fff;opacity:.6}
.calc-bg{position:absolute;top:1010px;left:0;width:458px;height:287px;background:linear-gradient(90deg,#6f7d86,#c9cfd2 45%,#e7ecef 70%,#b7c4cc)}
.calc{position:absolute;left:13px;top:1055px;width:210px;height:232px;background:var(--navy);padding:12px 19px;color:#fff}
.calc h2{font:700 14px 'Poppins',sans-serif;color:var(--yellow)}
.lbl{font-size:6px;margin-top:7px}
.sel{height:17px;border-radius:9px;background:#3a5a8c;margin-top:4px;position:relative;font-size:6px;color:#cfd8e8;padding:4px 12px}
.sel::after{content:"";position:absolute;right:6px;top:4px;width:9px;height:9px;background:#c9d3e3;border-radius:2px}
.checks{display:grid;grid-template-columns:1fr 1fr;font-size:6px;row-gap:3px;margin-top:7px}
.checks span::before{content:"";display:inline-block;width:6px;height:6px;background:#5a78a6;margin-right:7px;vertical-align:-1px}
.trio{display:grid;grid-template-columns:1fr 1fr 1fr;gap:5px;font-size:6px;margin-top:10px}
.sum{height:18px;border-radius:9px;background:var(--yellow);margin-top:3px;font-size:5px;color:var(--navy);padding:5px 9px}
.partner{position:absolute;top:1350px;height:22px;background:#9aa3b1;border-radius:3px}
.foot{position:absolute;top:1412px;left:0;width:458px;height:88px;background:var(--navy);color:#fff}
.fcol{position:absolute;top:34px;font:700 8px 'Poppins',sans-serif}
.fcol p{font:400 6px 'Open Sans',sans-serif;color:#93a6c6;line-height:1.9;margin-top:5px}
.fbrand{position:absolute;left:346px;top:32px;width:100px;justify-content:center;font:700 9px 'Poppins',sans-serif;display:flex;align-items:center;gap:4px;white-space:nowrap}
.fbrand i{width:9px;height:9px;background:var(--orange);display:block}
</style>
</head>
<body>
<div class="stage">
<div class="page">

  <header class="head">
    <div class="logo-bg"></div>
    <div class="brand"><i></i>Marlo Tidy Yard</div>
    <div class="info" style="left:164px">218 Harbor Bend Rd,<br>Alden, OR 97011</div>
    <div class="info" style="left:277px"><b>NEED SUPPORT?</b>help@marlotidy.example</div>
    <div class="info" style="left:372px"><b>CALL US ON:</b><span class="phone">800-555-0142</span></div>
  </header>

  <nav class="nav"><span class="on">HOME</span><span>SERVICES</span><span>FEATURES</span><span>PROJECTS</span><span>INDUSTRIES</span><span>CONTACTS</span></nav>
  <div class="quote">GET A QUOTE!</div>

  <section class="hero" role="img" aria-label="Smiling site worker in yellow gloves clearing a construction site">
    <div class="seal"><h3>Certified Company</h3><p>Reliable Crews For Every<br>Job Site.</p><span>BOOK A CREW</span></div>
    <div class="disc">Discount<b>30%</b>first site visit</div>
    <svg class="arrow" style="left:20px" width="10" height="16"><path d="M8 1 2 8l6 7" stroke="#fff" stroke-width="1.5" fill="none"/></svg>
    <svg class="arrow" style="left:428px" width="10" height="16"><path d="M2 1l6 7-6 7" stroke="#fff" stroke-width="1.5" fill="none"/></svg>
  </section>
  <div class="tabs">
    <div class="tab t1">Operating<em>Hours</em></div>
    <div class="tab t2">General<em>Labor</em></div>
    <div class="tab t3">Site<em>Cleanup</em></div>
    <div class="tab t4">Site<em>Maintenance</em></div>
  </div>

  <div class="ph" style="left:38px;top:286px;width:145px;height:136px;background:linear-gradient(135deg,#f1d36a,#4a78c8 60%,#e5e8ee)" role="img" aria-label="Worker in hard hat and safety vest sweeping a site floor"></div>
  <div class="ph" style="left:130px;top:281px;width:53px;height:53px;background:var(--blue)" role="img" aria-label="Hard hat and broom icon"></div>
  <div class="abs" style="left:235px;top:298px;width:180px">
    <div class="kicker">Welcome to Our Site</div>
    <div class="title" style="margin-top:6px">Construction Services<br>That We Provide</div>
    <div class="para" style="margin-top:8px">We supply general labor, upkeep and cleanup for building sites, so your crews stay safe, on schedule and ready for every inspection.</div>
  </div>
  <div class="btn-y" style="left:235px;top:408px;width:101px;height:22px">GET IN TOUCH WITH US</div>

  <section class="work">
    <svg class="abs" style="top:-6px;left:0" width="458" height="20"><path d="M0 14Q120 0 240 8T458 4V20H0Z" fill="#eef1fb"/></svg>
  </section>
  <div class="center kicker" style="top:502px">Keep your site on track</div>
  <div class="center title" style="top:513px;font-size:15px">How We Work</div>

  <div class="ph" style="left:38px;top:569px;width:92px;height:90px;background:linear-gradient(135deg,#c4d4e6,#5b7ca8)" role="img" aria-label="Site manager making a phone call"></div>
  <div class="step-badge" style="left:31px;top:569px;background:var(--navy);color:var(--yellow)">step 1</div>
  <div class="ph" style="left:183px;top:556px;width:92px;height:86px;background:linear-gradient(135deg,#dfe4ea,#2bb7e6 60%,#f5d83a)" role="img" aria-label="Gloved worker clearing debris"></div>
  <div class="step-badge" style="left:174px;top:555px;background:var(--cyan);color:#fff">step 2</div>
  <div class="ph" style="left:324px;top:577px;width:92px;height:82px;background:linear-gradient(135deg,#efe7da,#6b4a3a)" role="img" aria-label="Contractor paying an invoice on a laptop"></div>
  <div class="step-badge" style="left:314px;top:570px;background:var(--yellow);color:var(--navy)">step 3</div>

  <div class="step-t" style="left:16px;top:667px">Give us a Call</div>
  <div class="step-p" style="left:29px;top:687px">Tell us about your site and schedule and we will call you back... <a>Click here</a></div>
  <div class="step-t" style="left:164px;top:656px">The Site Work</div>
  <div class="step-p" style="left:177px;top:677px">Our trained crews arrive on time, work safely and leave every area clear.</div>
  <div class="step-t" style="left:312px;top:667px">Easy Payment</div>
  <div class="step-p" style="left:325px;top:687px">Book &amp; pay online. We'll match you with a trusted, experienced site crew.</div>

  <section class="feat">
    <svg class="abs" style="top:-2px;left:0" width="458" height="16"><path d="M0 0H458V2Q300 12 160 6T0 10Z" fill="#eef1fb"/></svg>
    <div class="center" style="top:61px;font:700 17.5px 'Poppins',sans-serif;color:var(--yellow)">Featured Services</div>
    <div class="center" style="top:84px;font:italic 8px 'Poppins',sans-serif;color:#fff">What We Offer</div>
    <div class="card" style="left:13px;background:linear-gradient(135deg,#d9dfe8,#2f8fe0)" role="img" aria-label="Workers loading debris into a skip"></div>
    <div class="card" style="left:162px;background:linear-gradient(135deg,#eef2f4,#3f6fb8 60%,#8fd4f2)" role="img" aria-label="Worker washing new building windows"></div>
    <div class="card" style="left:311px;background:linear-gradient(135deg,#efece6,#c9c4ba)" role="img" aria-label="Industrial vacuum on a concrete floor"></div>
    <div class="card-l" style="left:13px">Debris Removal</div>
    <div class="card-l" style="left:162px">Post-Build Windows</div>
    <div class="card-l" style="left:311px">Dust &amp; Floor Cleanup</div>
    <div class="dots"><i></i><i></i><i></i></div>
  </section>

  <div class="calc-bg" role="img" aria-label="Worker cleaning fixtures in a finished building"></div>
  <form class="calc">
    <h2>Calculated Form</h2>
    <div class="lbl">Indicate type of site work</div>
    <div class="sel">---</div>
    <div class="lbl">Please check any of the following site areas you would like our crew to cover.</div>
    <div class="checks"><span>Interior</span><span>Exterior</span><span>Scaffold Area</span><span>Other Areas</span></div>
    <div class="trio"><span>Floor(s)?</span><span>Unit(s)?</span><span>Staircase(s)?</span></div>
    <div class="trio" style="margin-top:4px"><div class="sel" style="margin:0"></div><div class="sel" style="margin:0"></div><div class="sel" style="margin:0"></div></div>
    <div class="lbl" style="margin-top:14px">Sum</div>
    <div class="sum">0</div>
  </form>

  <div class="partner" style="left:30px;width:52px"></div>
  <div class="partner" style="left:110px;width:66px"></div>
  <div class="partner" style="left:194px;width:68px"></div>
  <div class="partner" style="left:286px;width:56px"></div>
  <div class="partner" style="left:366px;width:70px"></div>

  <footer class="foot">
    <div class="fcol" style="left:13px">Information<p>Alden, OR 97011,<br>United States<br>hello@marlotidy.example</p></div>
    <div class="fcol" style="left:124px">Our Services<p>General Labor<br>Site Cleanup<br>Site Maintenance</p></div>
    <div class="fcol" style="left:235px">Quick Links<p>About Company<br>Services<br>Pricing</p></div>
    <div class="fbrand"><i></i>Marlo Tidy Yard</div>
    <div class="abs" style="left:346px;top:66px;width:100px;font-size:6px;color:#93a6c6;text-align:center;line-height:1.5">A clean, safe site keeps your build moving. That's why</div>
  </footer>

</div>
</div>
</body>
</html>
```